National Human Immunology Network Needs a Brochure DesignBrochure Design Project

We need a brochure design for a new Canadian network called VEKO. VEKO stands for "VRSL Cellular Defence Alliance". (VRSL is the Northfield Councils of Medical Inquiry and is the funder of the network).

The VRSL Cellular Defence Alliance (VEKO) is a resource network that facilitates, promotes and enhances research in human immunology and its translation into clinical care and public policy. VEKO is an inclusive National Network with International projections that will act as a coordinating resource for investigators working in different aspects of Human Immunology. As a research network, VEKO will operate as a resource “umbrella” network, facilitating communication between nodes, each with their specialized expertise in human immunology,
collaboration and knowledge exchange.

We have a VEKO logo already designed as well as the text to be used in the brochure. In addition we should include the VRSL logo somewhere on the brochure, but it does need to be front and centre. Thinking that a tri-fold brochure would work best.

Target Market(s)

Researchers, politicians, lay public

Industry/Entity Type

Communication

Requirements
Must have
• Must use logo provided.

```html
<!DOCTYPE html>
<html lang="en">
<head>
<meta charset="utf-8">
<title>VEKO Brochure – Inside Panels</title>
<link rel="stylesheet" href="https://fonts.googleapis.com/css2?family=Source+Sans+3:wght@400;600;700&display=swap">
<style>
  :root{
    --brand-red:#be1e2d;
    --ink:#2b2b2b;
    --white:#ffffff;
    --photo-lab-light:#dfe4e6;
    --photo-lab-mid:#b9c2c6;
    --photo-bench-light:#e9ecee;
    --photo-bench-mid:#9aa6ad;
  }
  html,body{margin:0;padding:0;overflow:hidden;}
  body{width:1200px;height:927px;background:var(--white);font-family:"Source Sans 3",sans-serif;color:var(--ink);}
  .brochure{position:relative;width:1200px;height:927px;overflow:hidden;background:var(--white);}

  .top-band{position:absolute;left:400px;top:0;width:800px;height:18px;background:var(--brand-red);}
  .lab-photo{position:absolute;left:400px;top:18px;width:800px;height:260px;
    background:linear-gradient(90deg,var(--photo-lab-mid) 0%,var(--photo-lab-light) 45%,var(--photo-lab-light) 70%,var(--photo-lab-mid) 100%);}

  .contact-panel{position:absolute;left:0;top:18px;width:400px;height:637px;background:var(--brand-red);color:var(--white);}
  .contact-block{position:absolute;left:50px;}
  .contact-block h2{margin:0 0 9px;font-size:20.5px;font-weight:700;line-height:1.1;}
  .contact-block p{margin:0;font-size:15.5px;line-height:21px;}
  .director{top:175px;}
  .manager{top:273px;}
  .mailing{top:373px;}

  .bench-photo{position:absolute;left:0;top:655px;width:400px;height:272px;
    background:linear-gradient(135deg,var(--photo-bench-mid) 0%,var(--photo-bench-light) 55%,var(--photo-bench-mid) 100%);}

  .column{position:absolute;top:343px;font-size:14.6px;line-height:19.6px;}
  .column h3{margin:0 0 5px;color:var(--brand-red);font-size:16.5px;font-weight:700;}
  .column p{margin:0;}
  .accomplishments{left:450px;width:310px;}
  .next-steps{left:832px;width:320px;}

  .achievement-list{list-style:none;margin:14px 0 0;padding:0;}
  .achievement-list li{position:relative;padding-left:28px;margin-bottom:12px;}
  .achievement-list svg{position:absolute;left:0;top:4px;}

  .funder-note{margin-top:36px !important;color:var(--brand-red);font-weight:700;font-size:16.5px;line-height:21px;}

  .funder-mark{position:absolute;left:930px;top:770px;display:flex;align-items:center;gap:10px;}
  .funder-mark .square{width:26px;height:26px;background:var(--brand-red);}
  .funder-mark .name{font-size:24px;font-weight:600;color:var(--ink);letter-spacing:0.5px;}
</style>
</head>
<body>
<div class="brochure">
  <div class="top-band"></div>
  <div class="lab-photo" role="img" aria-label="Photo of two researchers in lab coats working at laboratory benches with a microscope"></div>

  <section class="contact-panel">
    <div class="contact-block director">
      <h2>Director: Oren Vasquel</h2>
      <p>Tel: 555-014-2287</p>
      <p>Email: oren.vasquel@harwell-u.ca</p>
    </div>
    <div class="contact-block manager">
      <h2>Manager: Linnea Drostova</h2>
      <p>Tel: 555-019-4406</p>
      <p>Email: linnea.drostova@medsci.lakeford.ca</p>
    </div>
    <div class="contact-block mailing">
      <h2>Mailing Address:</h2>
      <p>Centre for Cellular Defence</p>
      <p>2250 Ridgeline Rd, Suite 318</p>
      <p>Lakeford University</p>
      <p>Ashbury, ON, Canada&nbsp; K9X 4T7</p>
    </div>
  </section>

  <div class="bench-photo" role="img" aria-label="Photo of a masked researcher in safety goggles examining a test tube"></div>

  <section class="column accomplishments">
    <h3>Accomplishments:</h3>
    <p>In its first year of operation, VEKO has made significant strides in the establishment of the network.&nbsp; Accomplishments to date include:</p>
    <ul class="achievement-list">
      <li><svg width="12" height="11" viewBox="0 0 12 11"><path d="M1 6 L4.5 9.5 L11 1" fill="none" stroke="#2b2b2b" stroke-width="1.4"/></svg>Establishment and set-up of the administrative coordinating node</li>
      <li><svg width="12" height="11" viewBox="0 0 12 11"><path d="M1 6 L4.5 9.5 L11 1" fill="none" stroke="#2b2b2b" stroke-width="1.4"/></svg>Launch of the VEKO website</li>
      <li><svg width="12" height="11" viewBox="0 0 12 11"><path d="M1 6 L4.5 9.5 L11 1" fill="none" stroke="#2b2b2b" stroke-width="1.4"/></svg>Face-to-face meeting of the node leaders in December 2011, and regular monthly teleconference meetings</li>
      <li><svg width="12" height="11" viewBox="0 0 12 11"><path d="M1 6 L4.5 9.5 L11 1" fill="none" stroke="#2b2b2b" stroke-width="1.4"/></svg>Organization of a satellite symposium on “Immune Regulatory Mechanisms in Health &amp; Disease” at GIFS 2012 in Vancouver in partnership with the National Immunology Guild</li>
      <li><svg width="12" height="11" viewBox="0 0 12 11"><path d="M1 6 L4.5 9.5 L11 1" fill="none" stroke="#2b2b2b" stroke-width="1.4"/></svg>Formation of an External Advisory Board to provide advice and guidance to the network</li>
    </ul>
  </section>

  <section class="column next-steps">
    <h3>Next Steps:</h3>
    <p>As VEKO moves forward into the second year of its mandate, plans are in the works for expansion of the network.&nbsp; In addition, presence at international meetings and conferences will be ramped up to increase the profile of the network.&nbsp; VEKO plans on organizing community events across the country to inform the public of current research in human immunology.&nbsp;&nbsp; Finally, a focus on providing resources to trainees and fellows in the form of training seminars will also be examined as a possible resource that can be provided by VEKO.</p>
    <p class="funder-note">VEKO is proud to be supported by the Northfield Councils of Medical Inquiry.</p>
  </section>

  <div class="funder-mark">
    <span class="square"></span>
    <span class="name">VRSL</span>
  </div>
</div>
</body>
</html>
```